business card - Helicopter Flight Services, Flight School, etc.

We need a business card design for a new helicopter service.

We offer Helicopter Flight Services, Aerial Filming & Photography, Flight School, and Helicopter Tours. In that order.

Summit Bladecraft, Inc.
Harold Tessendy
SummitBladecraft@Lumenpost.com
303-555-0182

Based at the Coldbrook Airport in Marlowe Springs, CA. The final design should communicate integrity and safety. Pictures or logos at your discretion.

Card back side - surprise me.

```html
<!DOCTYPE html>
<html lang="en">
<head>
<meta charset="utf-8">
<title>Summit Bladecraft, Inc. — Business Card</title>
<link rel="stylesheet" href="https://fonts.googleapis.com/css2?family=Source+Sans+3:ital,wght@0,400;0,600;0,700;0,800;1,700&display=swap">
<style>
  :root {
    --backdrop: #e9ecef;
    --card-white: #ffffff;
    --brand-blue: #1f4f9c;
    --brand-blue-deep: #163f80;
    --wave-light: #2f6fb6;
    --back-center: #2c6aab;
    --back-edge: #1b4b89;
    --ink: #1b1b1b;
    --ink-soft: #2a2a2a;
  }
  * { box-sizing: border-box; margin: 0; padding: 0; }
  html, body {
    width: 1200px; height: 1000px; overflow: hidden;
    background: var(--backdrop);
    font-family: "Source Sans 3", "Myriad Pro", Arial, sans-serif;
  }
  .card {
    position: absolute; left: 265px; width: 665px; height: 397px;
    border-radius: 24px; overflow: hidden;
    box-shadow: 0 4px 10px rgba(0,0,0,0.25);
  }
  .card--front { top: 73px; background: var(--card-white); }
  .card--back {
    top: 533px;
    background: radial-gradient(circle at 50% 48%, var(--back-center) 0%, #25609f 40%, var(--back-edge) 100%);
  }
  .brand-name {
    position: absolute; font-weight: 800; white-space: nowrap;
    letter-spacing: 0.2px;
  }
  .card--front .brand-name {
    left: 33px; top: 122px; font-size: 34px; color: var(--brand-blue);
  }
  .card--back .brand-name {
    left: 0; right: 0; top: 218px; text-align: center;
    font-size: 46px; color: var(--card-white);
  }
  .services { position: absolute; left: 33px; top: 200px; }
  .services__title {
    font-size: 17px; font-weight: 700; font-style: italic; color: var(--ink);
    margin-bottom: 5px;
  }
  .services__list { list-style: none; }
  .services__list li {
    position: relative; font-size: 17px; color: var(--ink-soft);
    line-height: 23.5px; padding-left: 12px;
  }
  .services__list li::before {
    content: ""; position: absolute; left: 0; top: 10px;
    width: 6px; height: 6px; border-radius: 50%; background: var(--brand-blue);
  }
  .contact { position: absolute; right: 30px; top: 206px; text-align: right; }
  .contact__name { font-size: 21px; font-weight: 700; color: var(--ink); margin-bottom: 12px; }
  .contact__line {
    display: flex; justify-content: flex-end; align-items: center; gap: 6px;
    font-size: 16px; color: var(--ink-soft); line-height: 24px; white-space: nowrap;
  }
  .contact__icon { width: 15px; height: 15px; fill: var(--brand-blue); flex: none; }
  .front-wave { position: absolute; left: 0; bottom: 0; width: 665px; height: 70px; }
</style>
</head>
<body>

<section class="card card--front" aria-label="Card front">
  <div class="brand-name">Summit Bladecraft, Inc.</div>

  <div class="services">
    <p class="services__title">Our Servcies:</p>
    <ul class="services__list">
      <li>Flight Services</li>
      <li>Aerial Filming</li>
      <li>Photography</li>
      <li>Flight School</li>
      <li>Helicopter Tours</li>
    </ul>
  </div>

  <div class="contact">
    <p class="contact__name">Harold Tessendy</p>
    <p class="contact__line">303-555-0182
      <svg class="contact__icon" viewBox="0 0 16 16" aria-hidden="true"><path d="M12.5 10.2l-2 .6c-.3.1-.6 0-.8-.2L6.9 7.8c-.2-.2-.3-.5-.2-.8l.6-2c.1-.4-.1-.8-.5-.9L4.6 3.5c-.4-.1-.8.1-.9.4C2.9 6.4 4 9 5.9 10.8c1.9 1.9 4.4 3 6.9 2.2.4-.1.6-.5.5-.9l-.6-1.9c0 0 0 0-.2 0z"/></svg>
    </p>
    <p class="contact__line">SummitBladecraft@Lumenpost.com
      <svg class="contact__icon" viewBox="0 0 16 16" aria-hidden="true"><path d="M1 3.5h14v9H1z" /><path d="M1 3.5l7 5 7-5" fill="none" stroke="#fff" stroke-width="1.3"/></svg>
    </p>
    <p class="contact__line">Coldbrook Airport in Marlowe Springs, CA.
      <svg class="contact__icon" viewBox="0 0 16 16" aria-hidden="true"><path d="M8 1.5L0.5 8h2v6.5h4v-4h3v4h4V8h2z"/></svg>
    </p>
  </div>

  <svg class="front-wave" viewBox="0 0 665 70" preserveAspectRatio="none" aria-hidden="true">
    <path d="M0 22 C150 38 260 46 380 30 C480 16 580 8 665 10 L665 70 L0 70 Z" fill="var(--wave-light)"/>
    <path d="M0 30 C160 45 270 50 390 36 C490 24 590 16 665 18 L665 22 C590 20 490 28 390 40 C270 54 160 50 0 36 Z" fill="#ffffff"/>
    <path d="M0 40 C160 56 290 58 410 44 C510 32 600 30 665 32 L665 70 L0 70 Z" fill="var(--brand-blue-deep)"/>
  </svg>
</section>

<section class="card card--back" aria-label="Card back">
  <div class="brand-name">Summit Bladecraft, Inc.</div>
</section>

</body>
</html>
```